Bright Fern Landscape Services LLC
business cards, letterhead, and envelopes.
Bright Fern Landscape Services LLC -
Creative Brief
Simple
Lydia Harcourt
Owner
2187 NW 58th Ave. Ocala, Fl 34475
lharcourt@quillmesh.net
Would like to use my tagline somewhere not necessarily right under the logo.

```html
<!DOCTYPE html>
<html lang="en">
<head>
<meta charset="utf-8">
<title>Bright Fern Landscape Services LLC – Business Cards</title>
<link rel="stylesheet" href="https://fonts.googleapis.com/css2?family=Montserrat:wght@800&family=Open+Sans:wght@400;600&display=swap">
<style>
  :root {
    --green: #1f9a3c;
    --green-deep: #137a2c;
    --lime: #cfe200;
    --orange: #f7931e;
    --white: #ffffff;
    --charcoal: #2a2a2a;
    --rule: #b9b9b9;
    --ink: #333333;
  }
  * { box-sizing: border-box; margin: 0; padding: 0; }
  html, body { width: 1200px; height: 1021px; overflow: hidden; background: var(--white); }
  body { position: relative; font-family: "Open Sans", Arial, sans-serif; }

  .card { position: absolute; overflow: hidden; border: 2px solid var(--rule); }
  .card--front  { left: 335px; top: 33px;  width: 552px; height: 324px; background: var(--white); }
  .card--green  { left: 50px;  top: 368px; width: 508px; height: 310px; background: linear-gradient(120deg, var(--green-deep) 0%, var(--green) 40%, var(--lime) 100%); border: none; }
  .card--orange { left: 608px; top: 368px; width: 542px; height: 310px; background: var(--orange); border: none; }
  .card--white  { left: 50px;  top: 698px; width: 508px; height: 312px; background: var(--white); }
  .card--dark   { left: 608px; top: 698px; width: 542px; height: 312px; background: var(--charcoal); border: none; }

  .swoosh { position: absolute; left: 0; top: 0; width: 100%; height: 100%; }

  /* brand block: dot + name + tagline */
  .brand { display: flex; align-items: center; gap: 12px; }
  .brand__dot { border-radius: 50%; background: var(--orange); flex: none; }
  .brand__text { display: flex; flex-direction: column; }
  .brand__name {
    font-family: "Montserrat", Arial, sans-serif;
    font-weight: 800;
    line-height: 1.05;
    color: var(--green);
    text-transform: uppercase;
  }
  .brand__name span { display: block; }
  .brand__name .lead { font-size: 1.45em; }
  .tagline {
    font-weight: 600;
    text-transform: uppercase;
    letter-spacing: 0.02em;
    color: var(--green);
    margin-top: 5px;
    white-space: nowrap;
  }

  /* front card */
  .front-brand { position: absolute; left: 28px; top: 24px; }
  .front-brand .brand__dot { width: 26px; height: 26px; }
  .front-brand .brand__name { font-size: 15px; }
  .front-brand .tagline { font-size: 8px; margin-top: 3px; }

  .person { position: absolute; left: 0; right: 0; top: 132px; text-align: center; }
  .person__name { font-size: 23px; color: var(--green); font-weight: 400; }
  .person__role { font-size: 14px; color: var(--ink); margin-top: 2px; }
  .contact {
    position: absolute; right: 26px; bottom: 26px;
    text-align: right; color: var(--white);
    font-size: 12.5px; line-height: 1.55; font-style: normal;
  }

  /* back cards */
  .back-brand {
    position: absolute; inset: 0;
    display: flex; align-items: center; justify-content: center;
  }
  .back-brand .brand__dot { width: 34px; height: 34px; }
  .back-brand .brand__name { font-size: 22px; }
  .back-brand .tagline { font-size: 11px; }

  .card--green .brand__name, .card--green .tagline { color: var(--white); }
  .card--orange .brand__name { color: var(--green-deep); }
  .card--orange .tagline { color: var(--white); }
  .card--orange .brand__dot { background: var(--green-deep); }
  .card--dark .brand__name, .card--dark .tagline { color: var(--green); }
</style>
</head>
<body>

<section class="card card--front">
  <svg class="swoosh" viewBox="0 0 552 324" preserveAspectRatio="none" aria-hidden="true">
    <defs>
      <linearGradient id="leafBand" x1="0" y1="0" x2="1" y2="0">
        <stop offset="0" stop-color="#137a2c"/>
        <stop offset="0.55" stop-color="#1f9a3c"/>
        <stop offset="1" stop-color="#cfe200"/>
      </linearGradient>
    </defs>
    <path d="M0,228 C170,226 360,185 552,112 L552,158 C380,218 200,282 0,324 Z" fill="url(#leafBand)"/>
    <path d="M150,324 C300,262 430,212 552,168 L552,324 Z" fill="#f7931e"/>
  </svg>

  <div class="brand front-brand">
    <span class="brand__dot"></span>
    <div class="brand__text">
      <p class="brand__name"><span class="lead">Bright Fern</span><span>Landscape Services LLC</span></p>
      <p class="tagline">Growing simple spaces into something special</p>
    </div>
  </div>

  <div class="person">
    <p class="person__name">Lydia Harcourt</p>
    <p class="person__role">Owner</p>
  </div>

  <address class="contact">
    2187 NW 58th Ave.<br>
    Ocala, Fl 34475<br>
    Phone: (352) 418-7362<br>
    Email: lharcourt@quillmesh.net
  </address>
</section>

<section class="card card--green">
  <div class="back-brand">
    <div class="brand">
      <span class="brand__dot"></span>
      <div class="brand__text">
        <p class="brand__name"><span class="lead">Bright Fern</span><span>Landscape Services LLC</span></p>
        <p class="tagline">Growing simple spaces into something special</p>
      </div>
    </div>
  </div>
</section>

<section class="card card--orange">
  <div class="back-brand">
    <div class="brand">
      <span class="brand__dot"></span>
      <div class="brand__text">
        <p class="brand__name"><span class="lead">Bright Fern</span><span>Landscape Services LLC</span></p>
        <p class="tagline">Growing simple spaces into something special</p>
      </div>
    </div>
  </div>
</section>

<section class="card card--white">
  <div class="back-brand">
    <div class="brand">
      <span class="brand__dot"></span>
      <div class="brand__text">
        <p class="brand__name"><span class="lead">Bright Fern</span><span>Landscape Services LLC</span></p>
        <p class="tagline">Growing simple spaces into something special</p>
      </div>
    </div>
  </div>
</section>

<section class="card card--dark">
  <div class="back-brand">
    <div class="brand">
      <span class="brand__dot"></span>
      <div class="brand__text">
        <p class="brand__name"><span class="lead">Bright Fern</span><span>Landscape Services LLC</span></p>
        <p class="tagline">Growing simple spaces into something special</p>
      </div>
    </div>
  </div>
</section>

</body>
</html>
```